Postcard Design

This card will promote the work of artist Dorian Fenwick
Front must be black bleed background, and feature the photo of a painting
Reverse text will show his name, web url and email address

Back will have the gallery logo on the left with space on the right for mailing address

Industry/Entity Type

Painting

```html
<!DOCTYPE html>
<html lang="en">
<head>
<meta charset="utf-8">
<title>Dorian Fenwick – Postcard Reverse</title>
<link href="https://fonts.googleapis.com/css2?family=Cinzel:wght@600&family=Source+Sans+3:wght@400;600&display=swap" rel="stylesheet">
<style>
  :root {
    --stage: #e6e6e6;
    --card: #ffffff;
    --ink: #3a3a3a;
    --ink-dark: #1e1e1e;
    --teal: #3d7884;
    --teal-deep: #2d5f6b;
    --cream: #efe8d2;
    --cream-deep: #e2d6b4;
    --stamp-line: #eadfc8;
  }
  * { box-sizing: border-box; margin: 0; padding: 0; }
  html, body { width: 1200px; height: 1000px; overflow: hidden; background: var(--stage); }
  .canvas { position: relative; width: 1200px; height: 1000px; }

  .postcard {
    position: absolute; left: 86px; top: 102px;
    width: 1028px; height: 795px;
    background: var(--card);
    box-shadow: 0 2px 6px rgba(0,0,0,.25);
  }

  .painting-texture {
    position: absolute; left: 25px; top: 255px;
    width: 978px; height: 515px;
    background: linear-gradient(to bottom, rgba(255,255,255,1) 0%, rgba(246,242,228,.9) 22%, var(--cream) 50%, var(--cream-deep) 100%);
  }

  .gallery-mark {
    position: absolute; left: 89px; top: 84px;
    width: 439px; height: 141px;
    border: 1.5px solid var(--ink-dark);
    font-family: "Source Sans 3", sans-serif;
  }
  .gallery-name {
    position: absolute; left: 12px; top: 14px;
    font-size: 62px; font-weight: 600; line-height: 1;
    letter-spacing: -1px; color: var(--ink-dark);
  }
  .gallery-tagline {
    position: absolute; left: 88px; top: 90px;
    font-size: 14px; color: var(--ink);
  }
  .gallery-address {
    position: absolute; right: 11px; top: 30px;
    text-align: right; font-size: 14.5px; line-height: 21px; color: var(--ink-dark);
  }
  .gallery-rule {
    position: absolute; left: 262px; right: 11px; top: 100px;
    border-top: 1.5px solid var(--ink-dark);
  }
  .gallery-web {
    position: absolute; right: 11px; top: 108px;
    font-size: 14.5px; color: var(--ink-dark);
  }

  .stamp-box {
    position: absolute; left: 722px; top: 48px;
    width: 256px; height: 212px;
    border: 1.5px solid var(--stamp-line); border-radius: 8px;
  }

  .artist-name {
    position: absolute; left: 108px; top: 318px;
    font-family: "Cinzel", serif; font-weight: 600;
    font-size: 64px; line-height: 1; letter-spacing: 1px;
    color: var(--teal);
    text-shadow: 0 1px 0 var(--teal-deep);
  }
  .contact {
    position: absolute; left: 110px;
    font-family: "Source Sans 3", sans-serif;
    font-size: 40px; color: var(--ink); letter-spacing: .2px;
  }
  .contact-web { top: 440px; }
  .contact-email { top: 530px; }

  .artist-signature {
    position: absolute; left: 130px; top: 630px;
    width: 720px; height: 130px;
    border-radius: 60px;
    background: radial-gradient(ellipse at center, rgba(61,120,132,.55) 0%, rgba(61,120,132,.25) 55%, rgba(61,120,132,0) 75%);
  }
</style>
</head>
<body>
<div class="canvas">
  <section class="postcard">
    <div class="painting-texture" role="img" aria-label="Close-up of cream textured paint surface from the artist's canvas"></div>

    <div class="gallery-mark">
      <div class="gallery-name">LINDEN</div>
      <div class="gallery-tagline">fine art &amp; craft gallery LLC</div>
      <div class="gallery-address">48 Harlow St<br>Brookfield, Pa 18400<br>570.555.0182</div>
      <div class="gallery-rule"></div>
      <div class="gallery-web">lindengalleryhaven.com</div>
    </div>

    <div class="stamp-box"></div>

    <h1 class="artist-name">Dorian Fenwick</h1>
    <p class="contact contact-web">www.lindengalleryhaven.com</p>
    <p class="contact contact-email">hello@lindengalleryhaven.com</p>

    <div class="artist-signature" role="img" aria-label="Artist's hand-painted teal signature on the canvas"></div>
  </section>
</div>
</body>
</html>
```